"Beyond Marrow Cay" Fictional Book Cover

BEYOND MARROW CAY
By: Dale Pruitt

Here's the intro .

"It had been nearly forty years since Ted Larraby last went to the island from where he was raised. Three months earlier he never would have thought about ever coming back. But life is weird. Things happen quickly and plans change, especially when your very life is at stake. The reason he was going back wasn’t to see old friends...no, no, no. They’re all dead. Of all the kids he grew up with on the island who moved off, he’s the only one still alive. Why?"

Pretty much all just a Lumeno book, by the way.

Target Market(s)

fiction readers

Requirements
Must have
• Somewhat of a dark, mysterious cover is what I'd like to see. Use your imagination. I've never written a fiction book before so I'm very open to ideas

Needs to have my name, DALE PRUITT at the bottom. like my other books, all of which are non-fiction
Nice to have
• Mysterious is what I'm looking for. NOT A HORROR story though. More a guy who left the island years ago, but is being called back to escape the rat race of modern, consumerist culture.

Please remember this NEEDS to jump out as a thumbnail on Bookvale as people are browsing. Mainly the WORDS need to stick out. Lighter words on a say a blue background.

If you want to try to use the attached pic, or something like this, to reflect an island in the cover, that'd be good.

I've also uploaded a couple images I purchased from Pixelcrate, hopefully you can make something work with these.

```html
<!DOCTYPE html>
<html lang="en">
<head>
<meta charset="utf-8">
<title>Beyond Marrow Cay — Dale Pruitt</title>
<link rel="stylesheet" href="https://fonts.googleapis.com/css2?family=Montserrat:wght@500;600&display=swap">
<style>
  :root {
    --sky-top: #2a57aa;
    --sky-low: #3467b8;
    --haze: #5081c4;
    --treeline: #2c5582;
    --treeline-light: #3f6a96;
    --buildings: #5c7fae;
    --pier: #4d6c9a;
    --pier-shadow: #2f4f7f;
    --water: #2a5aa5;
    --water-deep: #1d4891;
    --type: #ffffff;
  }
  html, body {
    margin: 0;
    padding: 0;
    width: 800px;
    height: 1200px;
    overflow: hidden;
    background: var(--sky-top);
  }
  .cover {
    position: relative;
    width: 800px;
    height: 1200px;
    overflow: hidden;
    background: linear-gradient(180deg, var(--sky-top) 0%, var(--sky-low) 55%, var(--haze) 64%);
    font-family: "Montserrat", "Helvetica Neue", Arial, sans-serif;
    color: var(--type);
  }
  .cover__scene {
    position: absolute;
    left: 0;
    top: 715px;
    width: 800px;
    height: 485px;
    background:
      radial-gradient(ellipse 260px 90px at 420px 200px, rgba(120,150,190,0.55), rgba(120,150,190,0) 100%),
      radial-gradient(ellipse 320px 60px at 330px 290px, rgba(110,135,170,0.6), rgba(110,135,170,0) 100%),
      linear-gradient(180deg,
        rgba(80,129,196,0) 0%,
        var(--haze) 5%,
        var(--treeline-light) 10%,
        var(--treeline) 20%,
        var(--treeline-light) 30%,
        var(--buildings) 42%,
        var(--pier) 55%,
        var(--pier-shadow) 68%,
        var(--water) 76%,
        var(--water-deep) 100%);
  }
  .cover__title {
    position: absolute;
    top: 58px;
    left: 0;
    width: 800px;
    margin: 0;
    text-align: center;
    font-weight: 600;
    font-size: 146px;
    line-height: 150px;
    letter-spacing: -0.015em;
  }
  .cover__title span { display: block; }
  .cover__author {
    position: absolute;
    top: 1084px;
    left: 0;
    width: 800px;
    margin: 0;
    text-align: center;
    font-weight: 500;
    font-size: 50px;
    line-height: 60px;
    letter-spacing: 0.03em;
  }
</style>
</head>
<body>
  <main class="cover">
    <div class="cover__scene" role="img" aria-label="Photo of an island ferry landing with wooden pier, small terminal buildings, trees and houses along the shore under blue sky, tinted blue"></div>
    <h1 class="cover__title">
      <span>BEYOND</span>
      <span>MARROW</span>
      <span>CAY</span>
    </h1>
    <p class="cover__author">DALE PRUITT</p>
  </main>
</body>
</html>
```